Business Card Design Project

We are a consulting company which works with tourism operators and attractions, wineries, heritage sites, National and conservation parks etc to help them identify their 'Point of Difference' and then deliver an exceptional tourism visitor experience.
We specialise in: Operator training, Site interpretation, Product and experience development, Planning and analysis.
We have a tag line of "Sharing every tale - done right."
The company name is MornVoice and the logo is this word with the 'Morn' in black and the 'Voice' in orange - but this can be changed. The 'a' is a speech bubble. A lot of what we do involves talking!
The design should communicate that we can make a big difference to the range and quality of experiences that visitors get at your site.
Updates

I put the wrong telephone number in my brief. My apologies.

It should be +61 0487 555 913

Target Market(s)

tourism busineses, wineries and cellar doors, heritage sites, environment managers, Government agencies & private companies

Industry/Entity Type

Tourism

Requirements
Must have
• Name: Ruth Pellow
Title: Adjunct Professor
Qualifications: BA(Hons), MSc
Role: Principal
Address: PO Box 317, Kelby Bay, Westmere 5190
Phone: (+61) 0487 555 913
Email: ruth@mornvoice-example.com.au
www.mornvoice-example.com.au
ABN 514 072 389 16

Operator Training, Site Interpretation, Product and Experience Development, Planning and Analysis.
Nice to have
• Awards:
Winner 2011 Coastline Visitor Honours – Kestrel College - Tourism Education and Training
Winner 2009 Coastline Visitor Honours - Outstanding Contribution by an Individual
Winner 2009 Gulfside Citizen Medal - Tourism Award
Should not have
• No 'shadows' to company name/logo please.
No black reverse side of card

```html
<!DOCTYPE html>
<html lang="en">
<head>
<meta charset="utf-8">
<title>MornVoice Consulting – Business Card</title>
<link rel="stylesheet" href="https://fonts.googleapis.com/css2?family=Open+Sans:wght@400;600;700&display=swap">
<style>
  :root {
    --ink: #1b1b1b;
    --orange: #e8821e;
    --grey: #5a5a5a;
    --card: #ffffff;
    --backdrop: #e4e4e4;
  }
  * { margin: 0; padding: 0; box-sizing: border-box; }
  html, body {
    width: 1200px;
    height: 900px;
    overflow: hidden;
    background: var(--backdrop);
    font-family: "Open Sans", Arial, sans-serif;
    color: var(--ink);
  }
  .canvas {
    position: relative;
    width: 1200px;
    height: 900px;
  }
  .card {
    position: absolute;
    left: 270px;
    width: 660px;
    height: 377px;
    background: var(--card);
    border: 1px solid #d2d2d2;
  }
  .card--logo { top: 48px; }
  .card--details { top: 473px; }

  /* Logo side */
  .brand-name {
    position: absolute;
    left: 46px;
    top: 88px;
    font-size: 92px;
    font-weight: 700;
    line-height: 1;
    letter-spacing: -2px;
    color: var(--ink);
  }
  .brand-descriptor {
    position: absolute;
    right: 50px;
    top: 196px;
    font-size: 30px;
    font-weight: 600;
    letter-spacing: 6px;
    color: var(--grey);
  }
  .tagline {
    position: absolute;
    left: 110px;
    top: 262px;
    font-size: 19px;
    font-weight: 600;
    color: var(--orange);
  }

  /* Details side */
  .contact {
    position: absolute;
    left: 40px;
    top: 34px;
    font-size: 13px;
    line-height: 1.45;
  }
  .contact__name {
    font-size: 19px;
    font-variant: small-caps;
    color: var(--orange);
    margin-bottom: 2px;
  }
  .contact__role { color: var(--ink); }
  .contact__lines { margin-top: 12px; }
  .contact__label { color: var(--orange); font-weight: 600; margin-right: 4px; }
  .contact__address {
    margin-top: 12px;
    display: flex;
    gap: 6px;
    align-items: flex-start;
  }
  .contact__address svg { flex: none; margin-top: 2px; }

  .mini-brand {
    position: absolute;
    left: 330px;
    top: 92px;
  }
  .mini-brand__name {
    font-size: 44px;
    font-weight: 700;
    line-height: 1;
    letter-spacing: -1px;
    color: var(--ink);
  }
  .mini-brand__descriptor {
    text-align: right;
    font-size: 14px;
    font-weight: 600;
    letter-spacing: 3px;
    color: var(--grey);
    margin-top: 2px;
  }
  .services {
    position: absolute;
    left: 332px;
    top: 186px;
    list-style: none;
    font-size: 16px;
    font-weight: 600;
    line-height: 1.3;
  }
  .services li {
    display: flex;
    gap: 10px;
    margin-bottom: 9px;
  }
  .services__marker {
    flex: none;
    width: 10px;
    height: 10px;
    margin-top: 6px;
    background: var(--orange);
  }
  .abn {
    position: absolute;
    right: 14px;
    top: 180px;
    font-size: 9px;
    letter-spacing: 0.5px;
    color: var(--grey);
    transform: rotate(90deg);
    transform-origin: right top;
    white-space: nowrap;
  }
</style>
</head>
<body>
<main class="canvas">
  <section class="card card--logo" aria-label="Card back">
    <div class="brand-name">MornVoice</div>
    <div class="brand-descriptor">CONSULTING</div>
    <p class="tagline">Sharing every tale - done right</p>
  </section>

  <section class="card card--details" aria-label="Card front">
    <div class="contact">
      <p class="contact__name">Ruth Pellow</p>
      <p class="contact__role">Adjunct Professor</p>
      <p class="contact__role">BA(Hons), MSc</p>
      <p class="contact__role">Principal</p>
      <div class="contact__lines">
        <p><span class="contact__label">p:</span>+61 0487 555 913</p>
        <p><span class="contact__label">e:</span>ruth@mornvoice-example.com.au</p>
        <p><span class="contact__label">w:</span>www.mornvoice-example.com.au</p>
      </div>
      <div class="contact__address">
        <svg width="11" height="15" viewBox="0 0 11 15" aria-hidden="true">
          <path d="M5.5 0C2.5 0 0 2.4 0 5.4 0 9.3 5.5 15 5.5 15S11 9.3 11 5.4C11 2.4 8.5 0 5.5 0z" fill="var(--orange)"/>
          <circle cx="5.5" cy="5.3" r="2" fill="#fff"/>
        </svg>
        <p>PO Box 317, Kelby Bay<br>Westmere 5190</p>
      </div>
    </div>

    <div class="mini-brand">
      <div class="mini-brand__name">MornVoice</div>
      <div class="mini-brand__descriptor">CONSULTING</div>
    </div>

    <ul class="services">
      <li><span class="services__marker"></span>Operator Training</li>
      <li><span class="services__marker"></span>Site Interpretation</li>
      <li><span class="services__marker"></span>Product and Experience<br>Development</li>
      <li><span class="services__marker"></span>Planning and Analysis</li>
    </ul>

    <p class="abn">ABN 514 072 389 16</p>
  </section>
</main>
</body>
</html>
```